Construction Machinery Company : needs two pages flyers to advertise "Demolition Tools"

>>UPDATE BRIEF

Hi Mr./ Ms, Designers,

To make your design work easier,
- I have updated the instruction (Please see attachment file 5 "Brief" , or below "Requirement session")
- I also re-upload the attachments. They are all photos and content for the design. Very Clear now.
- I have also increased the budget.

*More information, please go
www.quartz-ridge.com/spikeline

Hope you can work on my project.

>>Previous Brief
Hi Mr./ Ms. Designers,

We are an international construction machinery distributors, located in Hong Kong. Our client is HONG KONG contractors.
We want to start marketing "demolition tool" - the metal tool that used on excavator breaker.

We want the final designs export to two products
1) two pages A4 size flyers (Front for products, and Back for company info.)
2) one page 360mm x 265mm size advertisement (grouping products and company information together)
* design can be the same.

Requirement:
1) Tone: As construction industry is a very "man" industry, we want the flyer is very "METAL" theme.
(Our Company theme colour is RED, but you can use a new colour"

2) Theme: I want customer know we are PROFESSIONAL, SPECIALIST moil point seller, and we have a lot of experience.

3) Product message: we want the messages are
-TOUGHER,
-LONGER LIFE,
-LOWER PRICE,
-CONVENIENCE DELIVERY

4) Product: there are four kinds of "demolition tool", Moil Point, Wedge, Blunt, Cone. But I want to emphasis "Moil Point".

Remarks:
- To let you know what demolition tool is,
I have attached photos [teaching] for your reference.

- Beside the Product photos, we may put supplier's factory photos as background, to show it is a big factory.

- I have put many photo, as Source and for Reference.
Feel free to ask me questions.

- We may put "Chinese word" beside English in the end. I can send you the FONT file later.

Our website page:
http://quartz-ridge.com/spikeline/

Learning Reference:
http://www.brovantools.com/tools-parts.html

Target Market(s)

[Hong Kong] Construction Contractor user.

Industry/Entity Type

Construction Company

Requirements
Must have
• Theme: Since construction is a very "man" industry, Please have the theme "man and neat"
• two pages A4 size flyers

```html
<!DOCTYPE html>
<html lang="en">
<head>
<meta charset="utf-8">
<title>Quartz Ridge – Demolition Tools Flyer</title>
<link rel="stylesheet" href="https://fonts.googleapis.com/css2?family=Open+Sans:ital,wght@0,400;0,600;0,700;1,400&display=swap">
<style>
  :root {
    --red: #e0322c;
    --black: #050505;
    --white: #ffffff;
    --text-light: #e8e8e8;
    --rule: #4a4a4a;
    --photo-dark: #2a2d2c;
    --photo-mid: #5d6460;
    --photo-light: #8e958f;
  }
  * { margin: 0; padding: 0; box-sizing: border-box; }
  html, body { width: 1200px; height: 841px; overflow: hidden; background: var(--white); }
  body { position: relative; font-family: "Open Sans", Arial, sans-serif; color: var(--text-light); }

  .page { position: absolute; top: 0; height: 841px; overflow: hidden; background: var(--black); }
  .page--front { left: 0; width: 594px; }
  .page--back { left: 603px; width: 597px; }

  .header { position: absolute; top: 0; left: 0; right: 0; height: 68px; background: var(--black); }
  .header__title { position: absolute; right: 10px; top: 18px; font-size: 24px; font-weight: 600; color: var(--white); letter-spacing: 0.3px; line-height: 1; }
  .header__sub { position: absolute; right: 10px; top: 45px; font-size: 11px; font-weight: 700; color: var(--white); line-height: 1; }

  .hero-photo { position: absolute; top: 68px; left: 0; right: 0; height: 297px;
    background: linear-gradient(120deg, var(--photo-dark) 0%, var(--photo-mid) 45%, var(--photo-light) 80%, var(--photo-mid) 100%); }
  .hero-panel { position: absolute; top: 68px; left: 0; width: 100%; height: 297px; }

  .logo { position: absolute; top: 18px; left: 28px; width: 120px; height: 118px; background: var(--white);
    display: flex; flex-direction: column; align-items: center; justify-content: center; gap: 10px; }
  .page--back .logo { left: 30px; }
  .logo__dot { width: 34px; height: 34px; border-radius: 50%; background: var(--red); }
  .logo__name { font-size: 13px; font-weight: 700; color: var(--black); letter-spacing: 0.2px; }

  .usp-list { position: absolute; right: 22px; top: 116px; text-align: right; }
  .usp { margin-bottom: 22px; }
  .usp__title { font-size: 17px; color: var(--white); line-height: 1.2; }
  .usp__text { font-size: 13px; font-style: italic; color: var(--white); line-height: 1.35; }

  .about { position: absolute; right: 26px; top: 102px; width: 250px; text-align: right; color: var(--white); }
  .about__title { font-size: 18px; line-height: 22px; }
  .about__text { margin-top: 14px; font-size: 11.5px; line-height: 15px; text-align: center; }

  .lower-photo { position: absolute; top: 365px; left: 0; right: 0; bottom: 0;
    background: radial-gradient(ellipse at 40% 45%, #3b3f3e 0%, #242625 45%, #0e0f0f 100%); }

  .feature { position: absolute; display: flex; }
  .tick { position: absolute; width: 30px; height: 30px; }
  .feature__text { font-size: 12.5px; line-height: 18px; text-align: justify; color: var(--text-light); }
  .feature__lead { font-size: 13.5px; text-transform: uppercase; }
  .front-feature { left: 102px; width: 446px; }
  .back-feature { left: 102px; width: 446px; }

  .rule { position: absolute; height: 1px; background: var(--rule); }
  .section-title { position: absolute; font-size: 17px; color: var(--red); line-height: 1; }
  .moil-text { position: absolute; left: 44px; top: 712px; width: 504px; font-size: 14px; line-height: 18px; text-align: justify; color: var(--text-light); }

  .brand-strip { position: absolute; left: 37px; top: 705px; width: 520px; height: 56px; background: var(--white);
    display: flex; align-items: center; justify-content: space-around; padding: 0 12px; }
  .brand-mark { height: 12px; border-radius: 2px; background: #c9c9c9; }

  .contact { position: absolute; left: 0; right: 0; top: 785px; text-align: center; font-size: 12px; line-height: 19px; color: var(--text-light); }
  .contact__label { color: var(--red); }
</style>
</head>
<body>

<section class="page page--front">
  <div class="hero-photo" role="img" aria-label="Factory floor with stacks of moil point steel bars"></div>
  <svg class="hero-panel" viewBox="0 0 594 297" preserveAspectRatio="none" aria-hidden="true">
    <polygon points="330,0 594,0 594,297 275,297" fill="#e0322c"/>
  </svg>
  <header class="header">
    <div class="header__title">PROFESSIONAL</div>
    <div class="header__sub">SPECIALIST MOIL POINT SELLER</div>
  </header>
  <div class="logo"><span class="logo__dot"></span><span class="logo__name">QUARTZ RIDGE</span></div>

  <div class="usp-list">
    <div class="usp"><div class="usp__title">LOWER PRICE</div><div class="usp__text">Direct Import from Korea Production<br>Factory</div></div>
    <div class="usp"><div class="usp__title">LONGER LIFE</div><div class="usp__text">Superior-grade alloy steel, multistage<br>tempering</div></div>
    <div class="usp"><div class="usp__title">CONVENIENCE DELIVERY</div><div class="usp__text">We will send to your job site</div></div>
  </div>

  <div class="lower-photo" role="img" aria-label="Faded background of stacked steel tool bars in the factory"></div>

  <svg class="tick" style="left:44px;top:410px" viewBox="0 0 30 30" aria-hidden="true"><rect width="30" height="30" fill="#fff"/><path d="M7 15 L13 21 L23 8" stroke="#e0322c" stroke-width="4" fill="none"/></svg>
  <div class="feature front-feature" style="top:406px"><p class="feature__text"><span class="feature__lead">We cooperate with one of the biggest hammer tool factories</span> in Korea. Factory produces 50,000 pieces per month and exports them worldwide. Therefore, price is always attractive to customers.</p></div>

  <svg class="tick" style="left:44px;top:486px" viewBox="0 0 30 30" aria-hidden="true"><rect width="30" height="30" fill="#fff"/><path d="M7 15 L13 21 L23 8" stroke="#e0322c" stroke-width="4" fill="none"/></svg>
  <div class="feature front-feature" style="top:478px"><p class="feature__text"><span class="feature__lead">We insist in using superior-grade of alloy steel to keep good reputation.</span> We have advanced heat treatment facilities for multistage tempering procedure, plus carefully checks the finished tools, so that we can guarantee excellent strength and high toughness moil point.</p></div>

  <svg class="tick" style="left:44px;top:579px" viewBox="0 0 30 30" aria-hidden="true"><rect width="30" height="30" fill="#fff"/><path d="M7 15 L13 21 L23 8" stroke="#e0322c" stroke-width="4" fill="none"/></svg>
  <div class="feature front-feature" style="top:570px"><p class="feature__text">When placing your order, simply provide information of the moil points you need, and we will deliver them right at your jobsite.</p></div>

  <div class="rule" style="left:37px;top:679px;width:522px"></div>
  <div class="section-title" style="left:44px;top:693px">MOIL POINT</div>
  <p class="moil-text">Used for hard rocks or reinforced concrete, Generally suitable for splitting, May slip during hammering; therefore point must be stabilized.</p>
  <div class="rule" style="left:37px;top:767px;width:522px"></div>
</section>

<section class="page page--back">
  <div class="hero-photo" role="img" aria-label="Workshop with rack of moil points and tool cabinets"></div>
  <svg class="hero-panel" viewBox="0 0 597 297" preserveAspectRatio="none" aria-hidden="true">
    <polygon points="327,0 597,0 597,297 273,297" fill="#e0322c"/>
  </svg>
  <header class="header">
    <div class="header__title">PROFESSIONAL</div>
    <div class="header__sub">SPECIALIST MOIL POINT SELLER</div>
  </header>
  <div class="logo"><span class="logo__dot"></span><span class="logo__name">QUARTZ RIDGE</span></div>

  <div class="about">
    <div class="about__title">INTERNATIONAL<br>CONSTRUCTION<br>MACHINERY AND<br>EQUIPMENT DISTRIBUTOR</div>
    <p class="about__text">Quartz Ridge is an international construction machinery distributor, established since 2000. It has strived to provide global high quality construction machinery for contractors. By strength of professional knowledge, Quartz Ridge has now become one of the leading construction equipment distributors in Hong Kong</p>
  </div>

  <svg class="tick" style="left:47px;top:400px" viewBox="0 0 30 30" aria-hidden="true"><rect width="30" height="30" fill="#fff"/><path d="M7 15 L13 21 L23 8" stroke="#e0322c" stroke-width="4" fill="none"/></svg>
  <div class="feature back-feature" style="top:396px"><p class="feature__text"><span class="feature__lead">Global Machinery</span>With company global eye sight and expertise, Quartz Ridge proudly gets the honor sole distribution authorities from the best manufacturers. Also with all-rounded after sales service, it is able to form a well-established partnership with clients.</p></div>

  <svg class="tick" style="left:47px;top:475px" viewBox="0 0 30 30" aria-hidden="true"><rect width="30" height="30" fill="#fff"/><path d="M7 15 L13 21 L23 8" stroke="#e0322c" stroke-width="4" fill="none"/></svg>
  <div class="feature back-feature" style="top:485px"><p class="feature__text"><span class="feature__lead">Tunnelling Work</span><br>Presently, company focuses on tunneling machinery. With professional experience, Quartz Ridge is able to assist client by introducing global advanced tunnel equipment, to enhance levels of mechanization and modernization of tunnel projects.</p></div>

  <svg class="tick" style="left:47px;top:570px" viewBox="0 0 30 30" aria-hidden="true"><rect width="30" height="30" fill="#fff"/><path d="M7 15 L13 21 L23 8" stroke="#e0322c" stroke-width="4" fill="none"/></svg>
  <div class="feature back-feature" style="top:594px"><p class="feature__text"><span class="feature__lead">Mission</span> “Customer Comes First, Work Safe, Best Service” is the ideal we have committed all along, we always pay attention to our clients’ needs and proactively keep up with the world’s infrastructure development requirement, to enlarge our business scope.</p></div>

  <div class="rule" style="left:37px;top:679px;width:520px"></div>
  <div class="section-title" style="left:40px;top:685px">BRANDS</div>
  <div class="brand-strip" aria-label="Partner brands">
    <span class="brand-mark" style="width:72px"></span>
    <span class="brand-mark" style="width:62px;background:#e8a24a"></span>
    <span class="brand-mark" style="width:72px;background:#2a4a8c"></span>
    <span class="brand-mark" style="width:62px;background:#d23a35"></span>
    <span class="brand-mark" style="width:56px;background:#d23a35"></span>
    <span class="brand-mark" style="width:70px;background:#d23a35"></span>
  </div>
  <div class="rule" style="left:37px;top:767px;width:520px"></div>

  <div class="contact">
    <div>Unit 7, 3/F., Harbourfield Plaza, 18 Lok Wan Road, Tai Wai, Shatin, Hong Kong</div>
    <div><span class="contact__label">PHONE</span> +852 2555-0142 <span class="contact__label">FAX</span> +852 2555-0143 <span class="contact__label">EMAIL</span> info@quartz-ridge.com</div>
  </div>
</section>

</body>
</html>
```